Powerpoint Presentation Template

Kindly design a business class Powepoint Presentation template for our business use. Please stick to our company colours or even pictures as shown on our website and Logo

```html
<!DOCTYPE html>
<html lang="en">
<head>
<meta charset="utf-8">
<title>Lonvale Properties – Presentation Template</title>
<link href="https://fonts.googleapis.com/css2?family=Open+Sans:wght@400;600;700;800&display=swap" rel="stylesheet">
<style>
:root{
  --board:#8b8b8b;
  --maroon:#7e2418;
  --red:#a5322a;
  --red-deep:#8f2a20;
  --ink:#2a2a2a;
  --yellow:#f2b01e;
  --paper:#ffffff;
  --grey-text:#555;
}
*{box-sizing:border-box;margin:0;padding:0}
html,body{width:1200px;height:1200px;overflow:hidden;background:var(--board);font-family:"Open Sans",Arial,sans-serif;color:var(--ink)}
.board{position:relative;width:1200px;height:1200px}
.slide{position:absolute;background:var(--paper);overflow:hidden;box-shadow:2px 3px 6px rgba(0,0,0,.35)}
.slide.wide{width:256px;height:146px}
.slide.narrow{width:224px;height:124px}
.head{position:absolute;left:7%;top:7%}
.head h2{font-size:5.6px;font-weight:700;text-transform:uppercase;letter-spacing:.1px}
.head p{font-size:3.6px;text-transform:uppercase;color:var(--grey-text)}
.head::after{content:"";display:block;width:22px;height:1px;background:var(--red);margin-top:1.5px}
.brand{position:absolute;right:6%;top:6%;font-size:6px;font-weight:800;color:var(--maroon);text-align:right;line-height:1;text-transform:uppercase}
.foot{position:absolute;left:0;right:0;bottom:0;height:7px;background:var(--red-deep);display:flex;align-items:center;gap:14%;padding-left:3%;font-size:3px;color:#fff}
.foot::after{content:"";position:absolute;right:0;top:0;width:10%;height:100%;background:var(--ink)}
.foot .pg{position:absolute;right:2%;z-index:1}
.photo{position:absolute;background:linear-gradient(160deg,#7d9bbf 0%,#b7a58a 45%,#8b5b3c 100%)}
.photo.build{background:linear-gradient(170deg,#9db4cf 0%,#d8d2c6 40%,#6b4a3a 100%)}
.photo.site{background:linear-gradient(170deg,#6e8fb5 0%,#c28a55 55%,#7a4427 100%)}
.photo.dusk{background:linear-gradient(175deg,#3b4a62 0%,#a97c52 50%,#5b3a22 100%)}
.photo.inner{background:linear-gradient(160deg,#cfcfcf 0%,#8d8d8d 50%,#4a4a4a 100%)}
.panel{position:absolute;left:8%;right:7%;top:29%;bottom:13%;background:var(--red);box-shadow:1px 1px 3px rgba(0,0,0,.4)}
.panel .txt{position:absolute;left:5%;right:9%;top:9%;font-size:3.1px;line-height:1.4;color:#fff}
.panel .strip{position:absolute;left:0;right:7%;bottom:5%;height:42%;display:flex;gap:1.5%;padding:0 1.5%}
.panel .strip .photo{position:relative;flex:1;height:100%}
.panel .side{position:absolute;right:1%;top:10%;bottom:10%;width:5%;writing-mode:vertical-rl;transform:rotate(180deg);font-size:2.8px;color:#fff;text-transform:uppercase;text-align:center}
.panel .side.left{right:auto;left:1%}
.overlay-card{position:absolute;left:10%;right:10%;top:30%;bottom:20%;background:rgba(255,255,255,.9);padding:3% 3%;text-align:center}
.overlay-card h3{font-size:4.4px;color:var(--red);font-weight:700;text-transform:uppercase;margin-bottom:2px}
.overlay-card p{font-size:3.2px;line-height:1.45;color:var(--ink)}
.tiny{font-size:3.2px;line-height:1.4;color:var(--grey-text)}
.cover-name{position:absolute;right:42px;top:78px;text-align:right;color:var(--maroon);font-weight:800;line-height:1.05}
.cover-name .l1{font-size:26px}
.cover-name .l2{font-size:17px}
</style>
</head>
<body>
<main class="board">

<!-- Cover -->
<section class="slide cover" style="left:26px;top:50px;width:544px;height:305px">
  <svg width="544" height="305" viewBox="0 0 544 305" style="position:absolute;left:0;top:0">
    <defs>
      <linearGradient id="coverPhoto" x1="0" y1="0" x2="0" y2="1">
        <stop offset="0" stop-color="#4f6f92"/>
        <stop offset=".4" stop-color="#c99a5b"/>
        <stop offset=".7" stop-color="#7a3f22"/>
        <stop offset="1" stop-color="#3b2114"/>
      </linearGradient>
    </defs>
    <rect width="544" height="305" fill="#fff"/>
    <g role="img" aria-label="Excavator on a construction site under a dramatic sunset sky">
      <polygon points="0,0 290,0 360,305 0,305" fill="url(#coverPhoto)"/>
    </g>
    <polygon points="290,0 312,0 382,305 360,305" fill="var(--yellow)"/>
    <polygon points="0,268 544,214 544,305 0,305" fill="var(--red)"/>
    <rect x="0" y="262" width="544" height="0" fill="none"/>
    <polygon points="0,262 544,208 544,214 0,268" fill="var(--yellow)"/>
  </svg>
  <div class="cover-name"><p class="l1">LONVALE</p><p class="l2">PROPERTIES</p></div>
</section>

<!-- Our history -->
<section class="slide wide" style="left:26px;top:373px">
  <div class="head"><h2>Our History</h2><p>Lonvale Properties</p></div>
  <div class="brand">Lonvale<br>Properties</div>
  <div style="position:absolute;left:4%;top:30%;width:30%">
    <p style="font-size:3.6px;font-weight:700">OUR HISTORY</p>
    <p class="tiny">Founded in March 2005, Lonvale Properties is a fully owned construction and infrastructure company built on a base of steady local growth.</p>
  </div>
  <div class="photo build" role="img" aria-label="Company head office building" style="left:4%;top:56%;width:30%;height:28%"></div>
  <p style="position:absolute;left:48%;top:35%;font-size:10px;font-weight:800;color:var(--maroon)">JOURNEY</p>
  <svg style="position:absolute;left:36%;top:36%" width="150" height="60" viewBox="0 0 150 60">
    <path d="M5,50 C40,50 70,40 100,28 S135,8 145,3" fill="none" stroke="var(--red)" stroke-width=".8" stroke-dasharray="1.5 1.5"/>
    <g fill="var(--red)">
      <rect x="16" y="12" width="10" height="3"/><rect x="40" y="17" width="10" height="3"/><rect x="70" y="15" width="10" height="3"/><rect x="104" y="5" width="10" height="3"/><rect x="128" y="0" width="10" height="3"/>
      <rect x="30" y="56" width="10" height="3"/><rect x="54" y="55" width="10" height="3"/><rect x="86" y="47" width="10" height="3"/><rect x="114" y="38" width="10" height="3"/><rect x="128" y="20" width="10" height="3"/>
    </g>
    <g fill="#fff" font-family="Open Sans, sans-serif" font-size="2.4" font-weight="700">
      <text x="17" y="14.5">1997</text><text x="41" y="19.5">2001</text><text x="71" y="17.5">2004</text><text x="105" y="7.5">2016</text><text x="129" y="2.5">2018</text>
      <text x="31" y="58.5">2001</text><text x="55" y="57.5">2003</text><text x="87" y="49.5">2008</text><text x="115" y="40.5">2015</text><text x="129" y="22.5">2017</text>
    </g>
  </svg>
  <div class="foot"><span>+2710 555 0142</span><span>lonvale.example/properties</span><span>info@lonvale.example</span><span class="pg">4</span></div>
</section>

<!-- Stats -->
<section class="slide wide" style="left:310px;top:373px;background:var(--maroon)">
  <div style="position:absolute;left:0;top:12%;width:40%;text-align:center;color:#fff;line-height:1.2">
    <p style="font-size:4px">since inception in</p>
    <p style="font-size:10px;font-weight:600">March 2016</p>
    <p style="font-size:8px">OVER</p>
    <p style="font-size:10px;font-weight:700;color:var(--yellow)">77 MAJOR</p>
    <p style="font-size:7px;font-weight:700;color:var(--yellow)">CONSTRUCTION</p>
    <p style="font-size:5.5px;font-weight:700;color:var(--yellow)">PROJECT DELIVERED</p>
    <p style="font-size:8px">WORTH</p>
    <p style="font-size:10px;font-weight:700;color:var(--yellow)">$32 MILLION</p>
  </div>
  <div class="photo build" role="img" aria-label="Apartment block" style="left:44%;top:18%;width:19%;height:30%"></div>
  <div class="photo inner" role="img" aria-label="Modern house" style="left:64%;top:18%;width:19%;height:30%"></div>
  <div class="photo build" role="img" aria-label="White residential units" style="left:84%;top:18%;width:16%;height:30%"></div>
  <div class="photo site" role="img" aria-label="Parking canopy" style="left:44%;top:50%;width:19%;height:34%"></div>
  <div class="photo build" role="img" aria-label="Townhouse complex" style="left:64%;top:50%;width:19%;height:34%"></div>
  <div class="photo dusk" role="img" aria-label="Office interior" style="left:84%;top:50%;width:16%;height:34%"></div>
  <div class="foot"><span>+2710 555 0142</span><span>lonvale.example/properties</span><span>info@lonvale.example</span><span class="pg">5</span></div>
</section>

<!-- About -->
<section class="slide wide" style="left:26px;top:541px">
  <div class="head"><h2>About our Company</h2><p>Lonvale Properties</p></div>
  <div class="brand">Lonvale<br>Properties</div>
  <div class="photo site" role="img" aria-label="Workers building with timber on site" style="left:0;top:35%;width:100%;height:48%"></div>
  <div style="position:absolute;left:45%;top:37%;width:43%;height:44%;background:rgba(15,15,15,.9);color:#fff;padding:3% 3%">
    <p style="font-size:5px">OUR VISION</p>
    <div style="height:.5px;background:#fff;margin:1.5px 0"></div>
    <p style="font-size:3.4px;margin-bottom:6px;padding-left:3%">An infrastructure provider of distinction.</p>
    <p style="font-size:5px">OUR MISSION</p>
    <div style="height:.5px;background:#fff;margin:1.5px 0"></div>
    <p style="font-size:3.4px;padding-left:3%">Restore people's dignity through infrastructure development.</p>
  </div>
  <div class="foot"><span>+2710 555 0142</span><span>lonvale.example/properties</span><span>info@lonvale.example</span><span class="pg">2</span></div>
</section>

<!-- Values -->
<section class="slide wide" style="left:310px;top:541px">
  <div class="head"><h2>Our Values</h2><p>Lonvale Properties</p></div>
  <div class="brand">Lonvale<br>Properties</div>
  <div class="photo dusk" role="img" aria-label="Excavator at sunset" style="left:0;top:30%;width:47%;height:52%"></div>
  <div style="position:absolute;left:51%;top:35%;width:45%">
    <p class="tiny">In pursuit of our vision and mission, our values outline the path to our growth into a housing and infrastructure company that places our clients at the forefront of all we do:</p>
    <ul class="tiny" style="list-style:none;margin-top:4px;padding-left:4%">
      <li>➢ Professionalism</li><li>➢ Accountability</li><li>➢ Transparency</li><li>➢ Honesty</li>
    </ul>
  </div>
  <div class="foot"><span>+2710 555 0142</span><span>lonvale.example/properties</span><span>info@lonvale.example</span><span class="pg">3</span></div>
</section>

<!-- Services -->
<section class="slide wide" style="left:26px;top:704px">
  <div class="head"><h2>Our Services</h2><p>Lonvale Properties</p></div>
  <div class="brand">Lonvale<br>Properties</div>
  <div class="photo build" role="img" aria-label="Apartment building" style="left:0;top:22%;width:33%;height:32%"></div>
  <div class="photo site" role="img" aria-label="New road with red lanes" style="left:33.5%;top:22%;width:33%;height:32%"></div>
  <div class="photo build" role="img" aria-label="Residential estate" style="left:67%;top:22%;width:33%;height:32%"></div>
  <div style="position:absolute;left:0;top:55%;width:100%;height:40%;display:flex;gap:.5%">
    <div style="flex:1;background:var(--red);color:#fff;padding:2%"><p style="font-size:3.8px;font-weight:700;font-style:italic;margin-bottom:2px">BUILDING CONSTRUCTION</p><p style="font-size:2.8px;line-height:1.4">Over 16 years of building work across the region for public and private clients, from design to handover and project control.</p></div>
    <div style="flex:1;background:var(--red-deep);color:#fff;padding:2%"><p style="font-size:3.8px;font-weight:700;font-style:italic;margin-bottom:2px">ROAD &amp; CIVIL CONSTRUCTION</p><p style="font-size:2.8px;line-height:1.4">Turnkey civil works using our own plant: roads, earthworks, water, sanitation and civil structures for every client.</p></div>
    <div style="flex:1;background:var(--red);color:#fff;padding:2%"><p style="font-size:3.8px;font-weight:700;font-style:italic;margin-bottom:2px">PROPERTY DEVELOPMENT</p><p style="font-size:2.8px;line-height:1.4">We develop estates, apartment blocks, shared housing and business campuses as both owner and contractor.</p></div>
  </div>
  <div class="foot"><span>+2710 555 0142</span><span>lonvale.example/properties</span><span>info@lonvale.example</span><span class="pg">7</span></div>
</section>

<!-- Building construction overlay -->
<section class="slide wide" style="left:310px;top:704px">
  <div class="photo site" role="img" aria-label="Steel reinforcement on a building site" style="inset:0;bottom:7px"></div>
  <div class="overlay-card" style="top:30%;bottom:15%">
    <h3>Building Construction</h3>
    <p>Lonvale Properties has over 16 years' experience in building construction. Over the years we have completed building projects for public and private clients. Our skills cover Project Management, Design, Building Consulting and Sub-contractor Management. We have built homes, offices and industrial units, and public buildings for mining, health, water, retail and real estate clients.</p>
  </div>
  <div class="foot"><span>+2710 555 0142</span><span>lonvale.example/properties</span><span>info@lonvale.example</span><span class="pg">8</span></div>
</section>

<!-- Residential -->
<section class="slide wide" style="left:26px;top:867px">
  <div class="head"><h2>Building Construction</h2><p>Our Services</p></div>
  <div class="brand">Lonvale<br>Properties</div>
  <div class="panel">
    <div class="side left">Residential Buildings</div>
    <div class="txt" style="left:8%">From inception, our work with residential buildings has been valued and well recognised. We have built communities and helped provincial and state housing plans by completing low-cost housing and walk-up homes as well as buildings for national and municipal governments.</div>
    <div class="strip" style="left:6%;right:0">
      <div class="photo build" role="img" aria-label="Residential blocks"></div>
      <div class="photo" role="img" aria-label="Blue and white housing units"></div>
      <div class="photo site" role="img" aria-label="Housing under construction"></div>
    </div>
  </div>
  <div class="foot"><span>+2710 555 0142</span><span>lonvale.example/properties</span><span>info@lonvale.example</span><span class="pg">9</span></div>
</section>

<!-- Commercial -->
<section class="slide wide" style="left:310px;top:867px">
  <div class="head"><h2>Building Construction</h2><p>Our Services</p></div>
  <div class="brand">Lonvale<br>Properties</div>
  <div class="panel">
    <div class="side left">Commercial &amp; Industrial Buildings</div>
    <div class="txt" style="left:8%">As a company, Lonvale Properties keeps raising the standard in commercial and industrial development. We have completed office blocks, factories, malls, warehouses and steel structures in many provinces and build to each client's needs.</div>
    <div class="strip" style="left:6%;right:0">
      <div class="photo site" role="img" aria-label="Industrial site"></div>
      <div class="photo build" role="img" aria-label="Office block"></div>
      <div class="photo inner" role="img" aria-label="Steel frame interior"></div>
    </div>
  </div>
  <div class="foot"><span>+2710 555 0142</span><span>lonvale.example/properties</span><span>info@lonvale.example</span><span class="pg">10</span></div>
</section>

<!-- Service & public -->
<section class="slide wide" style="left:26px;top:1034px">
  <div class="head"><h2>Building Construction</h2><p>Our Services</p></div>
  <div class="brand">Lonvale<br>Properties</div>
  <div class="panel">
    <div class="side left">Service &amp; Public Buildings</div>
    <div class="txt" style="left:8%">Lonvale Properties is a trusted name in building service and public facilities across the region. We ensure our buildings meet high standards: schools, colleges, government offices, hospitals and clinics built to last.</div>
    <div class="strip" style="left:6%;right:0">
      <div class="photo build" role="img" aria-label="Public building"></div>
      <div class="photo dusk" role="img" aria-label="College building"></div>
      <div class="photo inner" role="img" aria-label="Clinic corridor"></div>
    </div>
  </div>
  <div class="foot"><span>+2710 555 0142</span><span>lonvale.example/properties</span><span>info@lonvale.example</span><span class="pg">11</span></div>
</section>

<!-- Civil overlay -->
<section class="slide wide" style="left:310px;top:1034px">
  <div class="photo dusk" role="img" aria-label="Excavator under a night sky" style="inset:0;bottom:7px;background:linear-gradient(175deg,#1d2f52 0%,#4a6d99 45%,#3a2a1e 100%)"></div>
  <div class="overlay-card" style="top:33%;bottom:14%">
    <h3>Civil Construction</h3>
    <p>Lonvale Properties has wide experience in turnkey solutions for civil projects. Using our own plant, we deliver roads and earthworks, water and sanitation, and civil structures. We keep growing in capacity and skill and aim to be a leading civil company known for timely delivery.</p>
  </div>
  <div class="foot"><span>+2710 555 0142</span><span>lonvale.example/properties</span><span>info@lonvale.example</span><span class="pg">12</span></div>
</section>

<!-- Right column -->
<section class="slide narrow" style="left:684px;top:30px">
  <div class="head"><h2>Civil Construction</h2><p>Our Services</p></div>
  <div class="brand">Lonvale<br>Properties</div>
  <div class="panel" style="top:28%">
    <div class="side">Roads and Earthworks</div>
    <div class="txt">Over the years we have completed many road and earthworks projects, including bus transit lanes and highway upgrades across the region. Our experience lets us deliver fine civil service.</div>
    <div class="strip"><div class="photo site" role="img" aria-label="Earthworks"></div><div class="photo" role="img" aria-label="Highway"></div><div class="photo site" role="img" aria-label="Road works"></div></div>
  </div>
  <div class="foot"><span>+2710 555 0142</span><span>lonvale.example</span><span>info@lonvale.example</span><span class="pg">13</span></div>
</section>

<section class="slide narrow" style="left:934px;top:30px">
  <div class="head"><h2>Civil Construction</h2><p>Our Services</p></div>
  <div class="brand">Lonvale<br>Properties</div>
  <div class="panel" style="top:28%">
    <div class="side">Water and Sanitation</div>
    <div class="txt">Lonvale Properties is known for large water and sanitation works, from pipelines and bulk supply to reticulation and sewer networks for towns across the region.</div>
    <div class="strip"><div class="photo site" role="img" aria-label="Trench excavation"></div><div class="photo" role="img" aria-label="Blue pipeline"></div><div class="photo site" role="img" aria-label="Workers on pipeline"></div></div>
  </div>
  <div class="foot"><span>+2710 555 0142</span><span>lonvale.example</span><span>info@lonvale.example</span><span class="pg">14</span></div>
</section>

<section class="slide narrow" style="left:684px;top:177px">
  <div class="head"><h2>Civil Construction</h2><p>Our Services</p></div>
  <div class="brand">Lonvale<br>Properties</div>
  <div class="panel" style="top:28%">
    <div class="side">Civil Structures</div>
    <div class="txt">Lonvale Properties is an expert civil structures firm. We have built bridges, dams and reservoirs, water plants and mining structures that meet world-class standards.</div>
    <div class="strip"><div class="photo site" role="img" aria-label="Concrete structure"></div><div class="photo inner" role="img" aria-label="Formwork"></div><div class="photo site" role="img" aria-label="Reservoir works"></div></div>
  </div>
  <div class="foot"><span>+2710 555 0142</span><span>lonvale.example</span><span>info@lonvale.example</span><span class="pg">15</span></div>
</section>

<section class="slide narrow" style="left:934px;top:177px">
  <div class="photo site" role="img" aria-label="Earthmover on a development site" style="inset:0;bottom:7px"></div>
  <div class="overlay-card" style="top:32%;bottom:22%">
    <h3>Property Development</h3>
    <p>Lonvale Properties works with Veldcore, a partner firm, on the development of real estate across the region. As owner and contractor we build gated estates, apartment blocks and business campuses.</p>
  </div>
  <div class="foot"><span>+2710 555 0142</span><span>lonvale.example</span><span>info@lonvale.example</span><span class="pg">16</span></div>
</section>

<section class="slide narrow" style="left:684px;top:323px">
  <div class="head"><h2>Property Development</h2><p>Our Services</p></div>
  <div class="brand">Lonvale<br>Properties</div>
  <div class="panel" style="top:28%">
    <div class="side">Civil Structures</div>
    <div class="txt">Lonvale Properties is skilled in turnkey property development, from land purchase and zoning through design, building and sales. With Veldcore we deliver a full service to clients.</div>
    <div class="strip"><div class="photo build" role="img" aria-label="Apartment block"></div><div class="photo build" role="img" aria-label="Townhouses"></div><div class="photo site" role="img" aria-label="Estate houses"></div></div>
  </div>
  <div class="foot"><span>+2710 555 0142</span><span>lonvale.example</span><span>info@lonvale.example</span><span class="pg">17</span></div>
</section>

<section class="slide narrow" style="left:934px;top:323px">
  <div class="brand">Lonvale<br>Properties</div>
  <div class="photo site" role="img" aria-label="Building site" style="left:34%;top:0;width:25%;height:30%"></div>
  <div class="photo" role="img" aria-label="Water treatment plant" style="left:0;top:40%;width:30%;height:50%"></div>
  <div class="photo inner" role="img" aria-label="Office interior" style="left:70%;top:40%;width:30%;height:50%"></div>
  <div class="photo site" role="img" aria-label="Trench works" style="left:34%;top:77%;width:25%;height:17%"></div>
  <div style="position:absolute;left:29%;top:36%;width:42%;height:40%;background:var(--red);color:#fff;text-align:center;display:flex;flex-direction:column;align-items:center;justify-content:center;gap:3px">
    <svg width="22" height="20" viewBox="0 0 22 20" aria-hidden="true"><rect x="1" y="4" width="20" height="15" rx="3" fill="none" stroke="#fff" stroke-width="1.6"/><rect x="7" y="1" width="8" height="4" rx="1" fill="#fff"/><circle cx="11" cy="11.5" r="4.5" fill="none" stroke="#fff" stroke-width="1.6"/><circle cx="11" cy="11.5" r="2" fill="#fff"/></svg>
    <p style="font-size:8px;font-weight:600">Our Gallery</p>
  </div>
  <div class="foot"><span>+2710 555 0142</span><span>lonvale.example</span><span>info@lonvale.example</span><span class="pg">18</span></div>
</section>

<section class="slide narrow" style="left:684px;top:471px">
  <div class="head"><h2>Portfolio</h2><p>Lonvale Properties</p></div>
  <div class="brand">Lonvale<br>Properties</div>
  <div class="photo build" role="img" aria-label="Residential building" style="left:0;top:38%;width:25%;height:50%"></div>
  <div class="photo inner" role="img" aria-label="Modern villa with pool" style="left:25%;top:33%;width:51%;height:60%"></div>
  <div class="photo site" role="img" aria-label="Construction site" style="left:76%;top:38%;width:24%;height:50%"></div>
  <div class="foot"><span>+2710 555 0142</span><span>lonvale.example</span><span>info@lonvale.example</span><span class="pg">19</span></div>
</section>

<section class="slide narrow" style="left:934px;top:471px">
  <div class="photo" role="img" aria-label="Road junction" style="left:0;top:0;width:65%;height:38%"></div>
  <div class="photo build" role="img" aria-label="White apartment block" style="left:65.5%;top:0;width:34.5%;height:80%"></div>
  <div class="photo dusk" role="img" aria-label="Brick apartment block" style="left:0;top:39%;width:32%;height:61%"></div>
  <div class="photo site" role="img" aria-label="Row of new houses" style="left:32.5%;top:81%;width:67.5%;height:19%"></div>
  <div class="brand" style="left:33%;right:35%;top:52%;text-align:center;font-size:7px">Lonvale<br>Properties</div>
</section>

<section class="slide narrow" style="left:684px;top:618px">
  <div class="head"><h2>1 Photo Portfolio</h2><p>Lonvale Properties</p></div>
  <div class="brand">Lonvale<br>Properties</div>
  <div class="photo inner" role="img" aria-label="Glass-fronted atrium interior" style="left:2%;top:26%;width:96%;height:64%"></div>
  <div style="position:absolute;left:4%;top:28%;width:20%;height:60%;background:var(--red);color:#fff;padding:2%">
    <p style="font-size:2.8px;font-weight:700;margin:4px 0 4px">PROJECT TITLE HERE</p>
    <p style="font-size:2.6px;line-height:1.4">Add a short note about this project, its client, its size and the year it was completed.</p>
  </div>
  <div class="foot"><span>+2710 555 0142</span><span>lonvale.example</span><span>info@lonvale.example</span><span class="pg">21</span></div>
</section>

<section class="slide narrow" style="left:934px;top:618px">
  <div class="photo dusk" role="img" aria-label="Excavator on site at sunset" style="inset:0;bottom:7px"></div>
  <div class="overlay-card" style="left:7%;right:7%;top:24%;bottom:18%">
    <p>Our team of professionals shares one view: every public, private or civil group plays a part in the growth of our country. We seek new ways to offer lasting and cost-effective housing and infrastructure, with <b>real value to our clients</b>. We are proud to have served <b>more than 13 000 families</b>.</p>
  </div>
  <div class="foot"><span>+2710 555 0142</span><span>lonvale.example</span><span>info@lonvale.example</span><span class="pg">6</span></div>
</section>

<!-- Closing -->
<section class="slide" style="left:684px;top:776px;width:479px;height:269px;background:#f3efea">
  <div class="photo inner" role="img" aria-label="Faded upward view of glass towers" style="inset:0;background:linear-gradient(90deg,#f0d9b8 0%,#f7f3ee 25%,#ffffff 50%,#f7f3ee 75%,#f0d9b8 100%);opacity:.9"></div>
  <div style="position:absolute;left:0;right:0;top:36%;text-align:center;color:var(--maroon);font-weight:800;line-height:1.05">
    <p style="font-size:38px">LONVALE</p>
    <p style="font-size:24px">PROPERTIES</p>
  </div>
</section>

</main>
</body>
</html>
```